Marlow Estate Group (Real Estate and Investment)

A high end, clean design.
We are a real estate company with sales, asset management and investment divisions. We want to use a black and white scheme which is really high end feel. The back of the card can just be the logo (black background with the white writing) as we will probably emboss this when we print)

Target Market(s)

High level investors, high end houses for sale

Industry/Entity Type

Business

Contact Information for Business Card

Name, position, phone number and email address
Ben Marlow, Managing Director, 0438926057 and ben@marlowestate.com.au

Requirements
Must have
• Back of the card to be the black background with the white writing (as per the attached images). Would like the capacity to emboss the writing and logo

```html
<!DOCTYPE html>
<html lang="en">
<head>
<meta charset="utf-8">
<title>Marlow Estate Group – Business Card</title>
<link rel="stylesheet" href="https://fonts.googleapis.com/css2?family=Open+Sans:wght@300;400;700&display=swap">
<style>
  :root {
    --backdrop: #1e1e1e;
    --card: #0b0b0b;
    --card-panel: #060606;
    --panel-edge: #161616;
    --ink: #ffffff;
    --ink-soft: #c9c9c9;
  }
  * { box-sizing: border-box; margin: 0; padding: 0; }
  html, body {
    width: 1200px; height: 900px; overflow: hidden;
    background: var(--backdrop);
    font-family: "Open Sans", Arial, sans-serif;
    color: var(--ink);
  }
  .stage {
    position: relative; width: 1200px; height: 900px;
    display: flex; align-items: center; justify-content: center; gap: 60px;
  }
  .card {
    position: relative; width: 500px; height: 290px;
    background: var(--card); border-radius: 24px; overflow: hidden;
  }
  /* Front */
  .card-front { display: flex; }
  .brand-panel {
    width: 46%; height: 100%;
    background: var(--card-panel);
    border-right: 1px solid var(--panel-edge);
    display: flex; align-items: center; justify-content: center; gap: 12px;
  }
  .brand-mark {
    width: 14px; height: 14px; border-radius: 50%;
    border: 1.5px solid var(--ink); flex: none;
  }
  .brand-name {
    font-size: 15px; font-weight: 400; letter-spacing: 2px; color: var(--ink);
    line-height: 1.35;
  }
  .details { padding: 46px 0 0 30px; }
  .person-name { font-size: 21px; font-weight: 700; line-height: 1.1; }
  .person-role { font-size: 14px; font-weight: 400; color: var(--ink-soft); margin-top: 4px; }
  .contact-list { list-style: none; margin-top: 30px; }
  .contact-list li {
    display: flex; align-items: center; gap: 12px;
    font-size: 15px; font-weight: 300; line-height: 1; margin-bottom: 9px;
  }
  .contact-icon { width: 12px; height: 12px; flex: none; fill: var(--ink); }
  /* Back */
  .card-back {
    display: flex; flex-direction: column; align-items: center; justify-content: center;
  }
  .back-mark {
    width: 64px; height: 64px; border-radius: 50%;
    border: 1.5px solid var(--ink); margin-bottom: 24px;
  }
  .back-name { font-size: 24px; font-weight: 400; letter-spacing: 1px; }
  .back-web { font-size: 12px; font-weight: 400; margin-top: 8px; letter-spacing: .5px; }
</style>
</head>
<body>
<main class="stage">
  <section class="card card-front" aria-label="Card front">
    <div class="brand-panel">
      <span class="brand-mark"></span>
      <span class="brand-name">MARLOW ESTATE<br>GROUP</span>
    </div>
    <div class="details">
      <h1 class="person-name">Ben Marlow</h1>
      <p class="person-role">Managing Director</p>
      <ul class="contact-list">
        <li>
          <svg class="contact-icon" viewBox="0 0 24 24" aria-hidden="true"><path d="M6.6 10.8a15.1 15.1 0 0 0 6.6 6.6l2.2-2.2c.3-.3.7-.4 1-.2 1.1.4 2.3.6 3.6.6.6 0 1 .4 1 1V20c0 .6-.4 1-1 1A17 17 0 0 1 3 4c0-.6.4-1 1-1h3.5c.6 0 1 .4 1 1 0 1.3.2 2.5.6 3.6.1.3 0 .7-.2 1z"/></svg>
          0438926057
        </li>
        <li>
          <svg class="contact-icon" viewBox="0 0 24 24" aria-hidden="true"><path d="M2 5h20v14H2z M3.5 6.5 12 13l8.5-6.5" fill="var(--ink)"/><path d="M3.5 6.5 12 13l8.5-6.5" fill="none" stroke="#0b0b0b" stroke-width="1.6"/></svg>
          ben@marlowestate.com.au
        </li>
        <li>
          <svg class="contact-icon" viewBox="0 0 24 24" aria-hidden="true"><circle cx="12" cy="12" r="10"/><path d="M2 12h20M12 2c3 3 3 17 0 20M12 2c-3 3-3 17 0 20" fill="none" stroke="#0b0b0b" stroke-width="1.4"/></svg>
          www.marlowestate.com.au
        </li>
      </ul>
    </div>
  </section>

  <section class="card card-back" aria-label="Card back">
    <span class="back-mark"></span>
    <p class="back-name">MARLOW ESTATE GROUP</p>
    <p class="back-web">www.marlowestate.com.au</p>
  </section>
</main>
</body>
</html>
```